Business Card Design

We are a General Practice - Family medicine
We also have Allied Health professionals working within our team

Industry/Entity Type

Business

Contact Information for Business Card

Front of the card to display:

BRAMBLEWICK MEDICAL
PHONE 6348 2917

5/41 Fennimore Parade
Launceston Tasmania 7284

Back of the card to display:

My Appointments
Date:
Time:
With:

Please remember to phone us on 6348 2917 to cancel your appointment if you can't keep it.
A fee applied to missed appointments

```html
<!DOCTYPE html>
<html lang="en">
<head>
<meta charset="utf-8">
<title>Bramblewick Medical – Business Card</title>
<link rel="stylesheet" href="https://fonts.googleapis.com/css2?family=Arimo&family=Carlito:wght@400;700&display=swap">
<style>
  :root {
    --paper: #ffffff;
    --ink: #4a4a4a;
    --ink-soft: #3a3a3a;
    --label: #222222;
    --cyan: #1ff0f5;
    --on-cyan: #ffffff;
  }
  html, body {
    margin: 0;
    padding: 0;
    overflow: hidden;
    background: var(--paper);
  }
  .canvas {
    position: relative;
    width: 1200px;
    height: 1171px;
    overflow: hidden;
    background: var(--paper);
    font-family: "Carlito", "Calibri", sans-serif;
    color: var(--ink);
  }
  .side-label {
    position: absolute;
    left: 0;
    font-family: "Arimo", "Arial", sans-serif;
    font-size: 36px;
    color: var(--label);
  }
  .side-label--front { top: 338px; }
  .side-label--back { top: 862px; }

  .brand-mark {
    position: absolute;
    left: 732px;
    top: 66px;
    width: 132px;
    height: 132px;
    background: var(--cyan);
  }
  .brand-name {
    position: absolute;
    left: 400px;
    width: 610px;
    top: 282px;
    text-align: center;
    font-size: 64px;
    font-weight: 700;
    letter-spacing: 1px;
    color: var(--ink);
    white-space: nowrap;
  }
  .contact-band {
    position: absolute;
    left: 237px;
    top: 480px;
    width: 963px;
    height: 90px;
    background: var(--cyan);
    color: var(--on-cyan);
    text-align: center;
    font-size: 23px;
    line-height: 30px;
    padding-top: 14px;
    box-sizing: border-box;
  }

  .appointments-title {
    position: absolute;
    left: 330px;
    width: 600px;
    top: 722px;
    text-align: center;
    font-size: 34px;
    font-weight: 700;
    color: var(--ink-soft);
  }
  .appointment-field {
    position: absolute;
    left: 489px;
    font-size: 27px;
    color: var(--ink);
    display: flex;
    align-items: baseline;
  }
  .appointment-field .blank {
    display: inline-block;
    border-bottom: 2px solid var(--ink);
    margin-left: 4px;
  }
  .appointment-field--date { top: 806px; }
  .appointment-field--date .blank { width: 210px; }
  .appointment-field--time { top: 885px; }
  .appointment-field--time .blank { width: 208px; }
  .appointment-field--with { top: 966px; }
  .appointment-field--with .blank { width: 208px; }

  .cancel-note {
    position: absolute;
    left: 300px;
    width: 900px;
    top: 1088px;
    text-align: center;
    font-size: 23px;
    line-height: 39px;
    color: var(--ink-soft);
  }
</style>
</head>
<body>
<main class="canvas">
  <section class="card card--front">
    <span class="side-label side-label--front">Front</span>
    <div class="brand-mark" aria-hidden="true"></div>
    <h1 class="brand-name">BRAMBLEWICK MEDICAL</h1>
    <div class="contact-band">
      PHONE 6348 2917&nbsp;&nbsp;&nbsp;5/41 Fennimore Parade<br>
      Launceston Tasmania 7284
    </div>
  </section>

  <section class="card card--back">
    <span class="side-label side-label--back">Back</span>
    <h2 class="appointments-title">My Appointments</h2>
    <div class="appointment-field appointment-field--date">Date:<span class="blank"></span></div>
    <div class="appointment-field appointment-field--time">Time:<span class="blank"></span></div>
    <div class="appointment-field appointment-field--with">With:<span class="blank"></span></div>
    <p class="cancel-note" style="margin:0">
      Please remember to phone us on 6348 2917 to cancel your appointment<br>
      if you can't keep it. A fee applied to missed appointments
    </p>
  </section>
</main>
</body>
</html>
```